Packaging & Label Design for CDB Products

We are a European CBD company specialising in athletic recovery, sleep improvement and wellness.

We would like the packaging to incorporate our logo and name (and font 'Codec') 'Meridell CBD'. The design must be transferable to all of our products. CBD Oils, Balms, Lip Balm and Vape E-Liquid.

We would like it to be simple but eye-catching and modern. We don't want bright colours. Preferred pallet of muted greys, blacks, white and pastel colours. Geometric concepts, possibly using different colours for each item of the range, we are open to new and fresh ideas (we are seeking you for your experience) and when we find the right design we would likely throw more work in your direction..

Our product range is not complete so the designer must be flexible with some changes and provide files where format can be easily edited by packaging manufacturer. We are also waiting for dimensions for the labels and boxes for several products and will supply the designer with full dimensions of all products once selected.

Oil Box: 2.6 x 9.0 x 2.6 cm (open format 16.7 x 11.6cm)
Labels: 7.8 x 3.3 cm (Front and Back)

Our expected product range will be:
CBD Oil 1000mg
CBD Oil 3000mg
CBD Balm 100mg
CBD Balm 300mg
E-Liquid 500mg
Lip Balm 50mg

We look forward to seeing your ideas.

Best Regards
Meridell CBD

```html
<!DOCTYPE html>
<html lang="en">
<head>
<meta charset="utf-8">
<title>Meridell CBD – Oil Packaging</title>
<link href="https://fonts.googleapis.com/css2?family=Montserrat:wght@400;500;700&display=swap" rel="stylesheet">
<style>
  :root{
    --bg:#ffffff;
    --panel-dark:#0d0d0d;
    --text-soft:#d6d6d6;
    --text-white:#f4f4f4;
    --text-muted:#a9a9a9;
  }
  *{margin:0;padding:0;box-sizing:border-box}
  html,body{width:1200px;height:1200px;overflow:hidden;background:var(--bg)}
  body{position:relative;font-family:"Montserrat",sans-serif}

  .panel{position:absolute;overflow:hidden;background:var(--panel-dark)}
  .panel-bg{position:absolute;inset:0;width:100%;height:100%}

  .box-front{left:590px;top:80px;width:420px;height:1020px}
  .bottle-label{left:150px;top:420px;width:360px;height:540px}

  .brand{position:absolute;font-weight:700;color:var(--text-soft);letter-spacing:.08em;white-space:nowrap}
  .product{position:absolute;font-weight:500;color:var(--text-muted);letter-spacing:.08em;white-space:nowrap}

  .box-front .brand{left:44px;top:92px;font-size:44px}
  .box-front .product{left:46px;top:152px;font-size:26px}
  .bottle-label .brand{left:34px;top:52px;font-size:30px}
  .bottle-label .product{left:36px;top:94px;font-size:18px}

  .logo-spot{position:absolute;display:flex;flex-direction:column;align-items:center;gap:14px;color:var(--text-white);font-weight:700;letter-spacing:.12em;white-space:nowrap}
  .logo-dot{border-radius:50%;background:var(--text-white)}
  .box-front .logo-spot{left:100px;top:470px;width:220px;font-size:19px}
  .box-front .logo-dot{width:26px;height:26px}
  .bottle-label .logo-spot{left:80px;top:250px;width:200px;font-size:14px;gap:10px}
  .bottle-label .logo-dot{width:18px;height:18px}

  /* vertical specs, reading bottom to top */
  .spec{position:absolute;writing-mode:vertical-rl;transform:rotate(180deg);white-space:nowrap;color:var(--text-muted)}
  .spec-volume{font-weight:500;letter-spacing:.06em;text-align:center;line-height:1.35}
  .spec-strength{font-weight:400;letter-spacing:.02em;line-height:1}
  .spec-strength small{margin-top:6px}

  .box-front .spec-volume{left:364px;top:410px;font-size:12px}
  .box-front .spec-strength{left:328px;top:492px;font-size:30px}
  .box-front .spec-strength small{font-size:13px}
  .bottle-label .spec-volume{left:296px;top:140px;font-size:10px}
  .bottle-label .spec-strength{left:288px;top:250px;font-size:22px}
  .bottle-label .spec-strength small{font-size:10px}

  .range-line{position:absolute;left:0;width:100%;text-align:center;color:var(--text-white);font-weight:500;letter-spacing:.14em;line-height:1.75}
  .box-front .range-line{bottom:72px;font-size:24px}
  .bottle-label .range-line{bottom:46px;font-size:15px}
</style>
</head>
<body>

<section class="panel box-front" aria-label="Oil box front panel">
  <svg class="panel-bg" viewBox="0 0 420 1020" preserveAspectRatio="none" aria-hidden="true">
    <defs>
      <linearGradient id="boxFacet" x1="1" y1="0" x2="0" y2="1">
        <stop offset="0" stop-color="#6a6a6a"/>
        <stop offset=".45" stop-color="#3a3a3a"/>
        <stop offset="1" stop-color="#1a1a1a"/>
      </linearGradient>
    </defs>
    <rect width="420" height="1020" fill="#0d0d0d"/>
    <polygon points="420,0 420,1020 0,1020 0,770" fill="url(#boxFacet)"/>
  </svg>
  <div class="brand">MERIDELL</div>
  <div class="product">CBD OIL</div>
  <div class="logo-spot"><span class="logo-dot"></span><span>MERIDELL CBD</span></div>
  <div class="spec spec-volume">( 30 ML )<br>1.02 FL OZ</div>
  <div class="spec spec-strength">1000<small>mg</small></div>
  <div class="range-line">FULL SPECTRUM<br>HEMP EXTRACTS</div>
</section>

<section class="panel bottle-label" aria-label="Bottle front label">
  <svg class="panel-bg" viewBox="0 0 360 540" preserveAspectRatio="none" aria-hidden="true">
    <defs>
      <linearGradient id="labelFacet" x1="1" y1="0" x2="0" y2="1">
        <stop offset="0" stop-color="#606060"/>
        <stop offset=".5" stop-color="#363636"/>
        <stop offset="1" stop-color="#181818"/>
      </linearGradient>
    </defs>
    <rect width="360" height="540" fill="#0d0d0d"/>
    <polygon points="360,0 360,540 0,540 0,420" fill="url(#labelFacet)"/>
  </svg>
  <div class="brand">MERIDELL</div>
  <div class="product">CBD OIL</div>
  <div class="logo-spot"><span class="logo-dot"></span><span>MERIDELL CBD</span></div>
  <div class="spec spec-volume">( 30 ML )<br>1.02 FL OZ</div>
  <div class="spec spec-strength">1000<small>mg</small></div>
  <div class="range-line">FULL SPECTRUM<br>HEMP EXTRACTS</div>
</section>

</body>
</html>
```